Byte Lantern Website

Design and implement (fully coded and ready to launch) website for a professional services company - please see the documents attached and send us an email if there are any questions
Target Market(s)
Market to potential clients about the services we offer and be able to reach us for any consulting opportunities
Industry/Entity Type
Professional Service
Coding
Coded - Design and coding required
Number of Pages Required
3 page
Requirements
Must have
- Single page website design that is SEO optimized
Blog Post
Contact US page
Cool images/ logos for the service offering - not fill the website with text/content
Must be professional looking website
Coded website should also look great on different screens - mobile, tablets etc
Nice to have
- Choose easy neutral colors that compliment the logo colors. Having said that don't use every color in the logo for the website design.
Should not have
- Too many colors and several various different fonts

```html
<!DOCTYPE html>
<html lang="en">
<head>
<meta charset="utf-8">
<title>Byte Lantern — Data Platforms, Analytics and Cloud Engineering</title>
<link rel="stylesheet" href="https://fonts.googleapis.com/css2?family=Raleway:wght@300;400;500;600;700;800&family=Playfair+Display:ital,wght@1,400;1,700&display=swap">
<style>
:root{
  --orange:#f0512a;
  --crimson:#d9254a;
  --purple:#6c4aa6;
  --blue:#1466c0;
  --navy:#1b2a55;
  --ink:#3a3a3a;
  --muted:#555;
  --footer:#2b2b2b;
  --strip:#f1f1f1;
  --white:#fff;
}
*{box-sizing:border-box;margin:0;padding:0}
html,body{width:1200px;height:3994px;overflow:hidden}
body{position:relative;font-family:"Raleway",sans-serif;color:var(--ink);background:var(--white)}
.abs{position:absolute}

/* header */
.site-header{position:absolute;left:0;top:0;width:1200px;height:60px;background:var(--white);box-shadow:0 1px 3px rgba(0,0,0,.12);z-index:3}
.brand{position:absolute;left:96px;top:18px;display:flex;align-items:center;gap:8px;font-weight:700;font-size:16px;color:#222;letter-spacing:.5px}
.brand-dot{width:12px;height:12px;border-radius:50%;background:var(--orange)}
.main-nav a{position:absolute;top:22px;font-size:11px;font-weight:600;letter-spacing:1px;color:#444;text-decoration:none}
.main-nav a.active{color:var(--blue)}
.nav-marker{position:absolute;left:706px;top:52px;width:0;height:0;border-left:8px solid transparent;border-right:8px solid transparent;border-bottom:8px solid var(--orange)}
.nav-divider{position:absolute;left:960px;top:4px;width:1px;height:52px;background:#ddd;transform:skewX(-15deg)}
.social{position:absolute;display:flex;gap:6px}
.social span{display:block;border-radius:50%}
.social.top{left:980px;top:18px}
.social.top span{width:22px;height:22px}
.s1{background:#3b5b9a}.s2{background:#2aa3dc}.s3{background:#4b6a8f}.s4{background:#d9252a}

/* hero */
.hero-photo{position:absolute;left:0;top:60px;width:1200px;height:540px;background:linear-gradient(100deg,#5b6b86 0%,#34466e 30%,#1f3060 55%,#152451 100%)}
.hero-title{position:absolute;left:653px;top:170px;color:var(--white);font-weight:700;line-height:1}
.hero-title .big{display:block;font-size:60px}
.hero-title .sub{display:block;font-size:42px;margin-top:2px}
.hero-text{position:absolute;left:654px;top:286px;width:430px;color:var(--white);font-size:16px;font-weight:500;line-height:25.5px}
.btn-pill{position:absolute;left:654px;top:388px;width:223px;height:54px;border-radius:27px;background:linear-gradient(90deg,var(--crimson),var(--orange));color:var(--white);font-size:12px;font-weight:800;letter-spacing:.5px;display:flex;align-items:center;padding-left:30px}
.hero-arrow{position:absolute;top:310px;width:53px;height:44px;background:var(--orange);opacity:.9}
.hero-arrow svg{display:block}
.hero-band{position:absolute;left:0;top:577px;width:1200px;height:51px;background:linear-gradient(90deg,var(--orange) 0%,var(--crimson) 40%,var(--purple) 70%,var(--crimson) 100%)}
.band-name{position:absolute;right:120px;top:591px;color:var(--white);font-size:18px;font-weight:700;letter-spacing:8px}

/* welcome */
.welcome-art{position:absolute;left:0;top:822px}
.eyebrow-line{position:absolute;left:527px;top:866px;width:124px;height:2px;background:var(--orange)}
.eyebrow{position:absolute;left:659px;top:854px;color:var(--orange);font-size:20px;font-weight:400;letter-spacing:4px}
.welcome-copy{position:absolute;left:527px;top:905px;width:580px;font-size:14.5px;line-height:25.5px;color:var(--muted)}
.welcome-copy p+p{margin-top:25px}

/* services */
.section-title{position:absolute;left:0;width:1200px;text-align:center;font-size:36px;font-weight:300;letter-spacing:3px;color:#222}
.service-card{position:absolute;top:1409px;width:282px;height:392px;background:var(--white);box-shadow:0 2px 14px rgba(0,0,0,.14)}
.service-icon{position:absolute;left:32px;top:25px;width:85px;height:85px;border-radius:50%;border:6px solid currentColor;display:flex;align-items:center;justify-content:center}
.service-icon span{width:52px;height:52px;border-radius:50%;background:currentColor;display:flex;align-items:center;justify-content:center}
.service-title{position:absolute;left:34px;top:120px;font-size:23px;font-weight:300;line-height:26px;letter-spacing:1px}
.service-text{position:absolute;left:36px;top:186px;width:215px;font-size:12.5px;line-height:20px;color:var(--muted)}
.btn-solid{position:absolute;left:36px;top:313px;width:155px;height:40px;color:var(--white);font-size:13px;display:flex;align-items:center;justify-content:center;letter-spacing:.5px}
.c-orange{color:var(--orange)}.c-crimson{color:var(--crimson)}.c-purple{color:var(--purple)}
.bg-orange{background:var(--orange)}.bg-crimson{background:var(--crimson)}.bg-purple{background:var(--purple)}

/* member */
.member-bg{position:absolute;left:0;top:1976px}
.member-title{position:absolute;left:0;top:2150px;width:1200px;text-align:center;color:var(--white);font-size:34px;font-weight:700}
.member-card{position:absolute;left:234px;top:2218px;width:710px;height:442px;background:var(--white)}
.member-photo{position:absolute;left:17px;top:17px;width:275px;height:408px;background:linear-gradient(160deg,#dfe3e6,#b9b0a6 55%,#8d8478)}
.member-bio{position:absolute;left:324px;top:34px;width:350px;font-family:"Playfair Display",serif;font-style:italic;font-weight:700;font-size:13.2px;line-height:27px;color:#222}
.member-bio .lead{font-size:23px;font-weight:400;color:var(--purple)}
.member-sign{position:absolute;left:320px;top:372px;font-family:"Playfair Display",serif;font-style:italic;font-weight:700;font-size:15px;letter-spacing:1px;color:#222}
.member-sign em{color:var(--purple)}

/* blog */
.blog-title{position:absolute;left:91px;top:2840px;font-size:34px;font-weight:700;color:#111}
.post{position:absolute;top:2906px;width:324px}
.post-photo{width:324px;height:228px;background:linear-gradient(135deg,#6e7680,#a8adb3 50%,#5c636b)}
.post-date{position:absolute;left:7px;top:8px;width:58px;height:59px;background:var(--orange);color:var(--white);padding:6px 0 0 9px;line-height:1}
.post-date b{display:block;font-size:25px;font-weight:700}
.post-date small{display:block;font-size:10px;letter-spacing:.5px;margin-top:4px}
.post h3{margin-top:22px;font-size:19px;font-weight:600;color:var(--orange)}
.post p{margin-top:12px;padding-left:2px;font-size:13.2px;line-height:22px;color:#222;font-weight:500}
.btn-outline{position:absolute;top:396px;left:0;width:133px;height:37px;border:2px solid #555;font-size:12px;display:flex;align-items:center;justify-content:center;letter-spacing:.5px;color:#333}
.btn-outline.filled{background:var(--orange);border-color:#d53f1b;color:var(--white)}

/* partners */
.partners{position:absolute;left:0;top:3399px;width:1200px;height:101px;background:var(--strip)}
.partner-arrow{position:absolute;top:39px;width:22px;height:22px;border:2px solid var(--orange);border-radius:50%}
.badge{position:absolute;top:34px;height:32px;background:#d7d7d7;border-radius:4px}

/* footer */
.site-footer{position:absolute;left:0;top:3500px;width:1200px;height:494px;background:var(--footer);color:#ddd}
.footer-brand{position:absolute;left:96px;top:98px;display:flex;align-items:center;gap:10px;font-size:22px;font-weight:700;color:var(--white);letter-spacing:.5px}
.footer-about{position:absolute;left:96px;top:188px;width:245px;font-size:13.5px;line-height:21px}
.footer-heading{position:absolute;top:96px;font-size:12.5px;font-weight:700;letter-spacing:1px;color:var(--orange)}
.contact-item{position:absolute;left:406px;display:flex;gap:10px;font-size:13px;line-height:19px}
.contact-item svg{flex:none;margin-top:2px}
.footer-menu{position:absolute;left:736px;top:137px;list-style:none;font-size:13px}
.footer-menu li{height:30px}
.newsletter-input{position:absolute;left:887px;top:129px;width:217px;height:40px;border-radius:20px;background:var(--white);color:#666;font-size:12px;padding:13px 0 0 22px;letter-spacing:.5px}
.newsletter-btn{position:absolute;left:887px;top:180px;width:217px;height:39px;border-radius:20px;background:var(--orange);color:var(--white);font-size:12px;font-weight:700;display:flex;align-items:center;justify-content:center}
.copyright{position:absolute;left:0;top:359px;width:1200px;text-align:center;font-size:13px}
.copyright span{color:var(--orange)}
.social.bottom{left:516px;top:391px;gap:8px}
.social.bottom span{width:36px;height:36px}
</style>
</head>
<body>

<header class="site-header">
  <div class="brand"><span class="brand-dot"></span>Byte Lantern</div>
  <nav class="main-nav">
    <a class="active" style="left:696px">HOME</a>
    <a style="left:778px">BLOG</a>
    <a style="left:854px">CONTACT US</a>
  </nav>
  <div class="nav-marker"></div>
  <div class="nav-divider"></div>
  <div class="social top" aria-label="Social links"><span class="s1"></span><span class="s2"></span><span class="s3"></span><span class="s4"></span></div>
</header>

<section class="hero">
  <div class="hero-photo" role="img" aria-label="Engineers with a laptop in a server room"></div>
  <div class="hero-arrow" style="left:19px"><svg width="53" height="44" viewBox="0 0 53 44"><path d="M38 22H15M22 15l-7 7 7 7" stroke="#fff" stroke-width="2" fill="none"/></svg></div>
  <div class="hero-arrow" style="left:1133px"><svg width="53" height="44" viewBox="0 0 53 44"><path d="M15 22h23M31 15l7 7-7 7" stroke="#fff" stroke-width="2" fill="none"/></svg></div>
  <h1 class="hero-title"><span class="big">Byte</span><span class="sub">Lantern provides</span></h1>
  <p class="hero-text">end to end services in architecture, design and development of Data Platforms, Analytic workloads, Data Engineering, Cloud Engineering</p>
  <div class="btn-pill">LEARN MORE</div>
  <div class="hero-band"></div>
  <div class="band-name">BYTE LANTERN</div>
</section>

<section class="welcome">
  <svg class="welcome-art" width="495" height="370" viewBox="0 0 495 370">
    <polygon points="325,0 491,0 470,28 305,28" fill="#f0512a"/>
    <polygon points="0,28 470,28 387,335 0,335" fill="#2d3a52" role="img" aria-label="Two engineers reviewing a laptop in a data centre"/>
    <polygon points="0,210 120,210 90,310 0,310" fill="#c65a2a" opacity=".6"/>
    <polygon points="215,338 378,338 364,367 203,367" fill="#f0512a"/>
  </svg>
  <div class="eyebrow-line"></div>
  <h2 class="eyebrow">WELCOME TO BYTE LANTERN</h2>
  <div class="welcome-copy">
    <p>Byte Lantern is a company which intends to be in front of the client's needs, deeply understanding clients' business and delivering and optimizing solutions from the initial phase of scoping the requirements, up to the final delivery, maintenance and continuous upgrade. Byte Lantern focuses always from the customer perspective to grasp their business need for the IT solutions they deliver.</p>
    <p>Our team operates with enthusiasm and flexibility. We are focused on our customers, being their reliable partner for services and solutions, working together on a partnership basis, helping clients with challenging problems to solve.</p>
  </div>
</section>

<section class="services">
  <h2 class="section-title" style="top:1322px">OUR SERVICES</h2>
  <article class="service-card" style="left:138px">
    <div class="service-icon c-orange"><span><svg width="26" height="18" viewBox="0 0 26 18"><path d="M6 16a5 5 0 0 1 0-10 7 7 0 0 1 13 1 4.5 4.5 0 0 1 1 9z" fill="#fff"/></svg></span></div>
    <h3 class="service-title c-orange">Platform<br>Architecture</h3>
    <p class="service-text">Byte Lantern is a company which intends to be in front of the client's needs, deeply understanding clients' business and delivering and optimizing solutions</p>
    <div class="btn-solid bg-orange">READ MORE</div>
  </article>
  <article class="service-card" style="left:462px">
    <div class="service-icon c-crimson"><span><svg width="26" height="22" viewBox="0 0 26 22"><path d="M2 16l6-7 5 5 9-11" stroke="#fff" stroke-width="2" fill="none"/></svg></span></div>
    <h3 class="service-title c-crimson">Data<br>Engineering</h3>
    <p class="service-text">Byte Lantern is a company which intends to be in front of the client's needs, deeply understanding clients' business and delivering and optimizing solutions</p>
    <div class="btn-solid bg-crimson">READ MORE</div>
  </article>
  <article class="service-card" style="left:780px">
    <div class="service-icon c-purple"><span><svg width="22" height="24" viewBox="0 0 22 24"><rect x="3" y="10" width="16" height="12" rx="2" fill="#fff"/><path d="M6 10V7a5 5 0 0 1 10 0v3" stroke="#fff" stroke-width="2" fill="none"/></svg></span></div>
    <h3 class="service-title c-purple">Cloud<br>Developments</h3>
    <p class="service-text">Byte Lantern is a company which intends to be in front of the client's needs, deeply understanding clients' business and delivering and optimizing solutions</p>
    <div class="btn-solid bg-purple">READ MORE</div>
  </article>
</section>

<section class="member">
  <svg class="member-bg" width="1200" height="820" viewBox="0 0 1200 820"><polygon points="0,152 1200,0 1200,820 0,820" fill="#1466c0"/></svg>
  <h2 class="member-title">Our Member</h2>
  <div class="member-card">
    <div class="member-photo" role="img" aria-label="Portrait of the founder in a grey shirt"></div>
    <p class="member-bio"><span class="lead">Arun manages</span> all the client interactions and engineering team at Byte Lantern. Arun has over 15 years of experience in the technology before he founded Byte Lantern. He managed development of large scale enterprise wide, high performance, scalable, real-time software solutions in Tele-communications, Gaming, Finance, and Insurance Industries. He spends time working on open source projects, contributions to Kestrel Store, Ember JobRunner and other projects. In free time, Arun enjoys travelling to historical places, playing sports - run, bike, tennis, ping-pong and spending time with family.</p>
    <div class="member-sign">Arun Velkar – <em>Founder</em></div>
  </div>
</section>

<section class="blog">
  <h2 class="blog-title">Blog</h2>
  <article class="post" style="left:95px">
    <div class="post-photo" role="img" aria-label="Team of colleagues standing together in an office"></div>
    <div class="post-date"><b>13</b><small>MARCH</small></div>
    <h3>Consulting Project</h3>
    <p>Dynamically target high-payoff intellectual capital for customized technologies. Objectively integrate emerging core competencies.</p>
    <div class="btn-outline filled">READ MORE</div>
  </article>
  <article class="post" style="left:437px">
    <div class="post-photo" role="img" aria-label="Smiling team group photo in a bright office"></div>
    <div class="post-date"><b>13</b><small>MARCH</small></div>
    <h3>Consulting Project</h3>
    <p>Dynamically target high-payoff intellectual capital for customized technologies. Objectively integrate emerging core competencies.</p>
    <div class="btn-outline">READ MORE</div>
  </article>
  <article class="post" style="left:781px">
    <div class="post-photo" role="img" aria-label="Two colleagues discussing work at a desk"></div>
    <div class="post-date"><b>13</b><small>MARCH</small></div>
    <h3>Consulting Project</h3>
    <p>Dynamically target high-payoff intellectual capital for customized technologies. Objectively integrate emerging core competencies.</p>
    <div class="btn-outline">READ MORE</div>
  </article>
</section>

<section class="partners" aria-label="Technology partners">
  <div class="partner-arrow" style="left:93px"></div>
  <div class="badge" style="left:166px;width:132px"></div>
  <div class="badge" style="left:327px;width:145px"></div>
  <div class="badge" style="left:498px;width:88px"></div>
  <div class="badge" style="left:612px;width:132px"></div>
  <div class="badge" style="left:768px;width:113px"></div>
  <div class="badge" style="left:890px;width:133px"></div>
  <div class="partner-arrow" style="left:1083px"></div>
</section>

<footer class="site-footer">
  <div class="footer-brand"><span class="brand-dot"></span>Byte Lantern</div>
  <p class="footer-about">Byte Lantern provides end to end services in architecture, design and development of Data Platforms, Analytic workloads, Data Engineering, Cloud Engineering</p>

  <h4 class="footer-heading" style="left:406px">CONTACT DETAILS</h4>
  <div class="contact-item" style="top:135px"><svg width="16" height="20" viewBox="0 0 16 20"><path d="M8 1a6 6 0 0 0-6 6c0 5 6 12 6 12s6-7 6-12a6 6 0 0 0-6-6z" fill="#f5a623"/><circle cx="8" cy="7" r="2.3" fill="#2b2b2b"/></svg><span>Riverside Point, 14 Harbour Walk,<br>Northgate, London<br>N4 2QX, United Kingdom</span></div>
  <div class="contact-item" style="top:207px"><svg width="18" height="18" viewBox="0 0 18 18"><path d="M4 1l3 4-2 2c1 3 3 5 6 6l2-2 4 3-2 3C8 17 1 10 1 3z" fill="#f5a623"/></svg><span>(310) 555-0148</span></div>
  <div class="contact-item" style="top:245px"><svg width="18" height="16" viewBox="0 0 18 16"><path d="M1 8l16-7-4 14-4-5z" fill="#f5a623"/></svg><span>hello@bytelantern.io</span></div>

  <h4 class="footer-heading" style="left:736px">MENU</h4>
  <ul class="footer-menu"><li>Home</li><li>About Us</li><li>Services</li><li>Testimonials</li><li>Contact us</li></ul>

  <h4 class="footer-heading" style="left:890px">SIGN UP FOR NEWSLETTER</h4>
  <div class="newsletter-input">Enter your email id</div>
  <div class="newsletter-btn">Subscribe Now</div>

  <p class="copyright">Copyright © 2020 <span>Byte Lantern</span></p>
  <div class="social bottom" aria-label="Social links"><span class="s1"></span><span class="s2"></span><span class="s3"></span><span class="s4"></span></div>
</footer>

</body>
</html>
```